elearning course template

Our company has a variety of elearning courses. We are currently redesigning the courses and are looking for a new layout for the online learning courses. The layout should be 800x600 and it needs to incorporate the following elements:
1. Course Name
2. Chapter Name
3. Page name
4. Our company logo (see attached file)
5. Navigation bar that includes:
- Next / back buttons
- Page count
- Audio control bar (see attached file)
- Menu items that include: "Menu, Transcript, Resources"
9. Exit button (may be included on the navigation bar if appropriate)
10. Content area must be 775 wide x 442 high

We would like to see designs that use our company colors, blue (RGB 0,69,144) and orange (RGB 222, 111, 51) and dark gray. We're looking for a solution that is clean, crisp and very user friendly. We'd also like to see a little dimension in the layout, we feel that our current layout is very "flat".

You can find out more about our company at www.fenlark-vro.com.

Industry/Entity Type

Graphic Design

```html
<!DOCTYPE html>
<html lang="en">
<head>
<meta charset="utf-8">
<title>Course Template</title>
<link rel="stylesheet" href="https://fonts.googleapis.com/css2?family=Jost:wght@500;700;800&family=Exo+2:wght@400&display=swap">
<style>
:root{
  --blue:#004590;
  --blue-dark:#0a2f7a;
  --blue-light:#2f6fd0;
  --orange:#de6f33;
  --panel:#e6e7e8;
  --frame-line:#8a8a8a;
  --white:#ffffff;
  --ink:#1b1b1b;
  --track:#d9d9d9;
}
*{box-sizing:border-box;margin:0;padding:0}
html,body{width:1135px;height:1200px;overflow:hidden;background:var(--white)}
.stage{position:relative;width:950px;height:1004px;transform:scale(1.1947);transform-origin:0 0}
.frame{position:absolute;left:18px;top:12px;width:922px;height:760px;border:1px solid var(--frame-line);overflow:hidden;
  background:
    radial-gradient(ellipse 140px 60px at 215px 680px,#ffb24a 0%,#e0531a 35%,rgba(120,20,10,0) 100%),
    radial-gradient(ellipse 260px 90px at 690px 690px,#d84a1c 0%,rgba(110,20,10,0) 100%),
    linear-gradient(180deg,#1c0a06 0%,#3a0e08 55%,#6a1a0c 80%,#2a0805 100%)}
.nav-backdrop{position:absolute;inset:0}
.panel{position:absolute;left:0;top:0;width:922px;height:603px;background:var(--panel);border-bottom-left-radius:185px 150px}
.header-band{position:absolute;left:0;top:0;width:740px;height:150px;filter:drop-shadow(2px 3px 3px rgba(0,0,0,.35))}
.icon-btn{position:absolute;top:16px;width:36px;height:34px;border-radius:5px;
  background:linear-gradient(180deg,var(--blue-light),var(--blue-dark));box-shadow:1px 2px 3px rgba(0,0,0,.45);
  display:flex;align-items:center;justify-content:center}
.icon-btn.exit{left:14px}
.icon-btn.settings{left:78px}
.course-name{position:absolute;left:210px;top:10px;width:450px;text-align:center;font:800 40px/1.1 "Jost",sans-serif;color:var(--blue);letter-spacing:.5px;word-spacing:8px}
.brand{position:absolute;left:800px;top:22px;width:122px;display:flex;align-items:center;gap:5px;font:700 16px/1.05 "Jost",sans-serif;color:var(--blue)}
.brand-dot{width:10px;height:10px;border-radius:50%;background:var(--orange);flex:none}
.chapter-name,.page-name{position:absolute;top:84px;font:700 31px/1.1 "Jost",sans-serif;color:var(--orange)}
.chapter-name{left:71px}
.page-name{right:81px}
.content-area{position:absolute;left:75px;top:138px;width:773px;height:440px;background:var(--white);box-shadow:0 0 2px rgba(0,0,0,.15)}
.content-title{margin-top:24px;text-align:center;font:700 41px/1.1 "Jost",sans-serif;color:var(--orange)}
.progress{position:absolute;left:164px;top:585px;width:606px;height:11px;border-radius:6px;background:linear-gradient(180deg,#fff,#d2d2d2);box-shadow:inset 0 0 1px rgba(0,0,0,.5)}
.progress-fill{width:120px;height:100%;border-radius:6px;background:linear-gradient(180deg,var(--blue-light),var(--blue-dark))}
.page-count{position:absolute;left:790px;top:581px;font:400 19px/1 "Exo 2",sans-serif;color:var(--blue)}
.audio{position:absolute;left:348px;top:631px;width:222px;height:18px;border-radius:3px;background:linear-gradient(180deg,#fbfbfb,#cfcfcf);
  display:flex;align-items:center;gap:6px;padding:0 5px;font:400 8px/1 sans-serif;color:var(--ink)}
.audio-track{flex:1;height:3px;background:#9a9a9a;position:relative}
.audio-track span{position:absolute;left:0;top:0;height:3px;width:46%;background:#111}
.nav-btn{position:absolute;top:696px;width:157px;height:24px;border:1px solid #6d8fd6;
  background:linear-gradient(180deg,#2d67c9,#0c3488);color:var(--white);font:400 15px/22px "Exo 2",sans-serif;text-align:center;box-shadow:0 1px 2px rgba(0,0,0,.5)}
.nav-btn.menu{left:131px}
.nav-btn.resources{left:369px}
.nav-btn.transcript{left:627px}
.arrow-btn{position:absolute;top:685px;width:58px;height:44px;border-radius:4px;border:1px solid #5b7fd0;
  background:linear-gradient(180deg,#3a7be0,#0a2f7a);box-shadow:1px 2px 3px rgba(0,0,0,.6);display:flex;align-items:center;justify-content:center}
.arrow-btn.back{left:21px}
.arrow-btn.next{left:830px}
</style>
</head>
<body>
<div class="stage">
  <div class="frame">
    <div class="nav-backdrop" role="img" aria-label="Glowing red and orange digital light background behind the navigation bar"></div>
    <div class="panel"></div>
    <svg class="header-band" viewBox="0 0 740 150" aria-hidden="true">
      <path d="M0 0 H700 A36 36 0 0 1 700 72 H120 C55 72 12 95 0 140 Z" fill="var(--orange)"/>
    </svg>
    <div class="icon-btn exit" aria-label="Exit">
      <svg width="18" height="18" viewBox="0 0 18 18"><path d="M3 3 L15 15 M15 3 L3 15" stroke="var(--orange)" stroke-width="4" stroke-linecap="round"/></svg>
    </div>
    <div class="icon-btn settings" aria-label="Settings">
      <svg width="18" height="18" viewBox="0 0 18 18"><circle cx="9" cy="9" r="5" fill="none" stroke="var(--orange)" stroke-width="4" stroke-dasharray="2.6 1.3"/><circle cx="9" cy="9" r="3.2" fill="var(--orange)"/></svg>
    </div>
    <h1 class="course-name">Course Name</h1>
    <div class="brand"><span class="brand-dot"></span>Fenlark VRO</div>
    <div class="chapter-name">Chapter Name</div>
    <div class="page-name">Page Name</div>
    <main class="content-area"><h2 class="content-title">Content Area</h2></main>
    <div class="progress"><div class="progress-fill"></div></div>
    <div class="page-count">10/29</div>
    <div class="audio">
      <svg width="6" height="7" viewBox="0 0 6 7"><rect width="2" height="7" fill="#111"/><rect x="4" width="2" height="7" fill="#111"/></svg>
      <span>00:10</span>
      <div class="audio-track"><span></span></div>
      <span>00:22</span>
      <svg width="22" height="8" viewBox="0 0 22 8"><path d="M0 3h2l2-2v6l-2-2H0z" fill="#111"/><path d="M8 5v1M10 4v2M12 3v3M14 2v4M16 1v5M18 1v6" stroke="#333" stroke-width="1"/></svg>
    </div>
    <div class="arrow-btn back" aria-label="Back">
      <svg width="44" height="30" viewBox="0 0 44 30"><path d="M3 15 L18 3 V10 H41 V20 H18 V27 Z" fill="none" stroke="var(--white)" stroke-width="2.5" stroke-linejoin="round"/></svg>
    </div>
    <div class="nav-btn menu">Menu</div>
    <div class="nav-btn resources">Resources</div>
    <div class="nav-btn transcript">Transcript</div>
    <div class="arrow-btn next" aria-label="Next">
      <svg width="44" height="30" viewBox="0 0 44 30"><path d="M41 15 L26 3 V10 H3 V20 H26 V27 Z" fill="none" stroke="var(--white)" stroke-width="2.5" stroke-linejoin="round"/></svg>
    </div>
  </div>
</div>
</body>
</html>
```